Morvadin Nutrition Supplement Jar

Label for jar. White label on a brown bottle jar.
Conservative look, should look like medicine.
Main Side:
Brightfield Health (smaller size) (with logo)
MORVADIN 10mg (large size)
Doctor Formulated
Developed in Clinical Practice
60 Capsules
(I prefer the single color white label with dark brown letters. Please stay close to that design)
(For the back side, please use the multicolor set up)
(The whole Label should be one color - white with dark brown letters)
Please visit my site for more inspiration and feel: www.calmorvex.com
The product will be brown jar listed on this site.
Can you please provide one version without the text "Brightfield Health & Logo".
Thank you.

Target Market(s)

Women, 34-59 years old

Industry/Entity Type

Nutrition

Requirements
Should not have
• Multicolors, leaves,

```html
<!DOCTYPE html>
<html lang="en">
<head>
<meta charset="UTF-8">
<title>Morvadin 10mg – Jar Label</title>
<link href="https://fonts.googleapis.com/css2?family=Rubik:wght@300;400;500;700&display=swap" rel="stylesheet">
<style>
  :root {
    --canvas-bg: #e9e9e9;
    --label-white: #ffffff;
    --brand-brown: #6e3b22;
    --band-dark: #3b1d10;
    --ink-brown: #4a2616;
    --text-white: #ffffff;
  }
  * { margin: 0; padding: 0; box-sizing: border-box; }
  html, body {
    width: 1200px;
    height: 960px;
    overflow: hidden;
    background: var(--canvas-bg);
    font-family: "Rubik", sans-serif;
  }
  .label {
    position: absolute;
    left: 250px;
    top: 52px;
    width: 700px;
    height: 856px;
    background: var(--label-white);
    color: var(--ink-brown);
    overflow: hidden;
  }
  .edge-band {
    position: absolute;
    left: 0;
    width: 100%;
    background: var(--brand-brown);
  }
  .edge-band--top { top: 0; height: 30px; border-top: 8px solid var(--band-dark); }
  .edge-band--bottom { bottom: 0; height: 26px; border-top: 6px solid var(--band-dark); }

  .brand-mark {
    position: absolute;
    top: 96px;
    left: 0;
    width: 100%;
    display: flex;
    justify-content: center;
    align-items: center;
    gap: 12px;
    font-size: 22px;
    font-weight: 400;
    color: var(--ink-brown);
  }
  .brand-mark__dot {
    width: 18px;
    height: 18px;
    border-radius: 50%;
    background: var(--ink-brown);
  }

  .product-name {
    position: absolute;
    left: 81px;
    top: 272px;
    display: flex;
    align-items: baseline;
    gap: 18px;
    white-space: nowrap;
  }
  .product-name__title {
    font-size: 78px;
    font-weight: 500;
    letter-spacing: 0;
    line-height: 1;
    color: var(--ink-brown);
  }
  .product-name__dose {
    font-size: 44px;
    font-weight: 300;
    color: var(--ink-brown);
  }
  .product-name__rule {
    position: absolute;
    left: 79px;
    top: 370px;
    width: 524px;
    height: 3px;
    background: var(--ink-brown);
  }
  .maker-name {
    position: absolute;
    left: 96px;
    top: 382px;
    font-size: 40px;
    font-weight: 300;
    color: var(--ink-brown);
    white-space: nowrap;
  }

  .claim-band {
    position: absolute;
    left: 0;
    top: 576px;
    width: 564px;
    height: 60px;
    background: var(--brand-brown);
    border-top: 8px solid var(--band-dark);
    border-bottom: 6px solid var(--band-dark);
    display: flex;
    align-items: center;
    padding-left: 137px;
    color: var(--text-white);
    font-size: 32px;
    font-weight: 500;
    letter-spacing: 0.5px;
    white-space: nowrap;
  }

  .origin-line {
    position: absolute;
    left: 70px;
    top: 748px;
    font-size: 25px;
    letter-spacing: 0.5px;
    color: var(--ink-brown);
    white-space: nowrap;
  }
  .origin-line__light { font-weight: 300; }
  .origin-line__regular { font-weight: 400; }

  .capsule-count {
    position: absolute;
    left: 569px;
    top: 740px;
    display: flex;
    align-items: center;
    gap: 4px;
    color: var(--ink-brown);
  }
  .capsule-count__text { display: flex; flex-direction: column; line-height: 1; }
  .capsule-count__number { font-size: 34px; font-weight: 700; }
  .capsule-count__unit { font-size: 10px; font-weight: 400; margin-top: 2px; }
</style>
</head>
<body>
  <main class="label">
    <div class="edge-band edge-band--top"></div>

    <div class="brand-mark">
      <span class="brand-mark__dot"></span>
      <span class="brand-mark__name">Brightfield Health</span>
    </div>

    <div class="product-name">
      <span class="product-name__title">MORVADIN</span>
      <span class="product-name__dose">10mg</span>
    </div>
    <div class="product-name__rule"></div>
    <div class="maker-name">Brightfield Health</div>

    <div class="claim-band">DOCTOR FORMULATED</div>

    <p class="origin-line">
      <span class="origin-line__light">DEVELOPED IN </span><span class="origin-line__regular">CLINICAL PRACTICE</span>
    </p>

    <div class="capsule-count">
      <svg class="capsule-count__icon" width="22" height="46" viewBox="0 0 22 46" aria-hidden="true">
        <rect x="2" y="2" width="18" height="42" rx="9" fill="none" stroke="currentColor" stroke-width="2.5"/>
        <path d="M2 23 V11 A9 9 0 0 1 20 11 V23 Z" fill="currentColor"/>
      </svg>
      <div class="capsule-count__text">
        <span class="capsule-count__number">60</span>
        <span class="capsule-count__unit">Capsules</span>
      </div>
    </div>

    <div class="edge-band edge-band--bottom"></div>
  </main>
</body>
</html>
```